依頼詳細
オープン前のプレオープンで使用するチラシ依頼です。
キャンペーン価格で5日間限定で初回は初見料と施術代で9000円が500円1日限定で10名

こんなお困りの症状はありませんか?

・整体やマッサージに通っているが、肩がこって仕事や日常生活がつらい
・腰痛で電気をあてたり、整骨院に行っても変化がなく諦めている
・頻繁に頭痛に襲われて辛いので、その度に頭痛薬を飲む
・生理前後に痛みが強く、鎮痛薬を飲んでしまう
・精神薬を処方されたが、いつまで飲み続けるのか不安だけどやめられない
・病院で薬をもらったが一向にめまいが改善しない
の項目はなるべく全部入れたいです。

女性に特化した整体院なのでそこがイメージしやすいデザインがありがたいです。
記載項目
店名:自律神経専門 整体院 ゆらぎ→自律神経専門を目立たせて欲しいです。

URL:https://yuragi-karada.example/

地図→詳細を送りますので作成して頂きたいです。

スタッフ写真もしくは女性が施術している写真を入れて欲しいです。

マンションの外装写真を入れるか目印のマルカワ堂がすぐ近く(ビル1つとなり)なので場所イメージがついたほうがいい気がするのでそこの情報はどちらか入れたいです。
電話番号とラインに関しては7月中に取得します。

院内
・予約優先制
・女性セラピスト指名OK
・施術ルーム完全個室
・キッズスペースあり
・ロゴ
を入れたいです。

サイズ
A4
ページ数
両面
希望イメージ
シンプル 複雑
単色 カラフル
暗い 明るい
日常 高級
遊び心 厳粛
未来的 伝統的
女性的 男性的
希望する色
赤系、緑系、茶系
納品ファイル
• 高解像度JPG (.jpg)
• PNG形式 (.png)
補足説明
可能であれば当社でも内容を修正することができれば助かります。
出来る限りインパクトの強いチラシが希望です。

「自律神経専門」整体院の自律神経専門が目立ちたいです。
宜しくお願い致します。

```html
<!DOCTYPE html>
<html lang="ja">
<head>
<meta charset="utf-8">
<title>自律神経専門 整体院 ゆらぎ プレオープン</title>
<link href="https://fonts.googleapis.com/css2?family=Shippori+Mincho:wght@600;800&family=Noto+Sans+JP:wght@400;700;900&family=Dancing+Script:wght@700&display=swap" rel="stylesheet">
<style>
:root{
  --paper:#fbf8f1;
  --green:#5fa83a;
  --green-dark:#2f6b2c;
  --green-pale:#e3f0d6;
  --rose-pale:#f7e3d6;
  --rose-dark:#a0472e;
  --brown:#4a3a2c;
  --line:#c9b9a6;
  --red:#d8342a;
  --photo-a:#e8dccd;
  --photo-b:#cdb9a3;
  --sky:#c9dbe8;
}
*{margin:0;padding:0;box-sizing:border-box}
html,body{width:849px;height:1200px;overflow:hidden;background:#fff}
.flyer{position:relative;width:849px;height:1200px;background:linear-gradient(180deg,var(--paper) 0%,#fff 60%,#f4f9ee 100%);font-family:"Noto Sans JP",sans-serif;color:var(--brown);overflow:hidden}

.hero-photo{position:absolute;left:250px;top:0;width:330px;height:390px;background:radial-gradient(ellipse at 50% 40%,var(--photo-a),var(--photo-b) 72%,transparent 73%);opacity:.9}
.specialty{position:absolute;left:22px;top:26px;font-family:"Shippori Mincho",serif;font-weight:800;font-size:30px;letter-spacing:3px;padding-bottom:6px;border-bottom:2px solid var(--brown)}
.logo{position:absolute;right:40px;top:22px;text-align:center;font-family:"Shippori Mincho",serif;font-weight:800;color:var(--brown)}
.logo-mark{width:36px;height:36px;border-radius:50%;background:var(--green);margin:0 auto 6px}
.logo-sub{font-size:20px;letter-spacing:4px}
.logo-name{font-size:44px;letter-spacing:4px;line-height:1.1}

.headline{position:absolute;left:0;top:262px;width:849px;display:flex;justify-content:space-between;padding:0 70px;font-family:"Shippori Mincho",serif;font-weight:800;font-size:110px;color:var(--green);line-height:1;text-shadow:0 0 8px #fff}
.verb{position:absolute;left:392px;top:200px;z-index:2;writing-mode:vertical-rl;font-family:"Shippori Mincho",serif;font-weight:800;color:var(--green-dark);font-size:24px;letter-spacing:8px;text-shadow:0 0 6px #fff}
.question{position:absolute;top:384px;left:0;width:849px;text-align:center;font-family:"Shippori Mincho",serif;font-weight:800;font-size:24px;letter-spacing:2px}

.symptoms{position:absolute;top:422px;left:36px;width:777px;display:grid;grid-template-columns:repeat(6,1fr);gap:6px}
.symptom{background:#fff;border:1px solid var(--line);height:222px}
.symptom h3{height:36px;display:flex;align-items:center;justify-content:center;text-align:center;font-size:12px;line-height:1.2;font-weight:700;padding:0 4px;background:var(--green-pale);color:var(--green-dark)}
.symptom:nth-child(even) h3{background:var(--rose-pale);color:var(--rose-dark)}
.symptom p{font-size:11px;line-height:1.6;padding:7px 8px}

.gallery{position:absolute;top:654px;left:36px;width:777px;height:150px;display:grid;grid-template-columns:1.4fr 1fr 1fr 1fr;gap:6px}
.gallery div{background:linear-gradient(135deg,var(--photo-a),var(--photo-b))}

.features{position:absolute;top:814px;left:36px;width:520px;display:grid;grid-template-columns:1fr 1fr;gap:6px}
.feature{height:40px;display:flex;align-items:center;justify-content:center;background:var(--green-dark);color:#fff;font-weight:900;font-size:21px;white-space:nowrap}

.campaign{position:absolute;left:36px;top:904px}
.campaign-en{font-family:"Dancing Script",cursive;font-size:56px;color:var(--green);line-height:1.1}
.campaign-ja{font-family:"Shippori Mincho",serif;font-weight:800;font-size:36px;line-height:1.2;color:var(--green-dark);margin-left:10px}
.limit{position:absolute;left:320px;top:924px;border:1px solid var(--brown);font-size:12px;padding:3px 8px;background:#fff;white-space:nowrap}
.price{position:absolute;left:60px;top:1026px;display:flex;align-items:flex-end;gap:18px}
.price-before{font-size:22px;font-weight:900;line-height:1.3;padding-bottom:8px}
.price-after{font-weight:900;color:var(--red);font-size:96px;line-height:.9}
.price-after small{font-size:40px}

.contact{position:absolute;left:36px;top:1140px;font-size:13px;line-height:1.7;font-style:normal}

.open-info{position:absolute;right:22px;top:820px;width:240px;text-align:right}
.access{font-size:13px;font-weight:700;line-height:1.5}
.open-date{font-family:"Shippori Mincho",serif;font-weight:800;color:var(--red);font-size:58px;line-height:1.05}
.open-label{font-family:"Shippori Mincho",serif;font-weight:800;color:var(--red);font-size:26px;letter-spacing:4px;line-height:1.2}
.building{position:absolute;left:572px;top:972px;width:148px;height:228px;background:linear-gradient(180deg,var(--sky),#e9eef2 55%,#d8d2c8)}
.landmark{position:absolute;left:728px;top:1060px;width:112px;font-size:12px;font-weight:700;line-height:1.5}
</style>
</head>
<body>
<main class="flyer">
  <div class="hero-photo" role="img" aria-label="ストレッチをする女性セラピストの写真"></div>
  <p class="specialty">自律神経専門</p>
  <div class="logo">
    <div class="logo-mark"></div>
    <p class="logo-sub">整体院</p>
    <p class="logo-name">ゆらぎ</p>
  </div>
  <h1 class="headline"><span>自</span><span>律</span><span>神</span><span>経</span></h1>
  <p class="verb">を整える</p>
  <h2 class="question">こんなお困りの症状はありませんか?</h2>

  <section class="symptoms">
    <div class="symptom"><h3>肩こり</h3><p>整体やマッサージに通っているが、肩がこって仕事や日常生活がつらい</p></div>
    <div class="symptom"><h3>改善されない</h3><p>腰痛で電気をあてたり、整骨院に行っても変化がなく諦めている</p></div>
    <div class="symptom"><h3>頭痛</h3><p>頻繁に頭痛に襲われて辛いので、その度に頭痛薬を飲む</p></div>
    <div class="symptom"><h3>生理痛</h3><p>生理前後に痛みが強く、鎮痛薬を飲んでしまう</p></div>
    <div class="symptom"><h3>正しい薬が<br>わからない</h3><p>精神薬を処方されたが、いつまで飲み続けるのか不安だけどやめられない</p></div>
    <div class="symptom"><h3>薬が合わない</h3><p>病院で薬をもらったが一向にめまいが改善しない</p></div>
  </section>

  <section class="gallery">
    <div role="img" aria-label="女性セラピストの施術風景の写真"></div>
    <div role="img" aria-label="首まわりの施術の写真"></div>
    <div role="img" aria-label="背中の施術の写真"></div>
    <div role="img" aria-label="骨盤まわりの施術の写真"></div>
  </section>

  <section class="features">
    <p class="feature">予約優先制</p>
    <p class="feature">女性セラピスト指名OK</p>
    <p class="feature">施術ルーム完全個室</p>
    <p class="feature">キッズスペース</p>
  </section>

  <section class="campaign">
    <p class="campaign-en">Pre-open</p>
    <p class="campaign-ja">キャンペーン価格</p>
  </section>
  <p class="limit">5日間限定・1日限定10名</p>
  <div class="price">
    <p class="price-before">初見料＋施術代<br>9,000円が</p>
    <p class="price-after">500<small>円!</small></p>
  </div>

  <address class="contact">
    〒000-0000 架空県緑市桜台1-2-3 サンプルビル1階<br>
    https://yuragi-karada.example/
  </address>

  <div class="open-info">
    <p class="access">みどりライン<br>桜台駅 徒歩3分</p>
    <p class="open-date">9/20</p>
    <p class="open-label">オープン</p>
  </div>
  <div class="building" role="img" aria-label="院が入るマンションの外観写真"></div>
  <p class="landmark">目印はビル1つとなり マルカワ堂のすぐ隣です!</p>
</main>
</body>
</html>
```